Packaging Design: Logo/Bottle Design for New Botanical Cocktail Brand

We are a new start up, looking to create a new line of Ready to drink Cocktails. The brand name is Verdelle Garden Cocktails, infused with fruit, herb, and floral botanicals grown on our farm in New Hampshire. Flavors will include: Herb flavored with cilantro, Berry- flavored with Alpine Strawberry, Citrus flavored with lemon Verbena & lemon balm, Pear flavored with Bartlett pear, Cucumber & Mint. We need a logo and a label design. There are 2 possible bottles to choose from.

Designer has complete freedom with everything! From fonts and colors to bottle caps and closures. Please view the pinterest link for inspirational bottle designs. https://www.pinboardly.example/kestrawynn/garden-drinks/

Target Market(s)

Female 21 to 48 years old. College educated and professional. The type of person that has a passion for a cause and eats and shops local. People that respect an artisan quality product, hand made by a master craftsman.

Industry/Entity Type

Floral

Requirements
Must have
• Clear Bottle, see options attached. You may also choose your own BUT WE MUST SEE THE LOGO AND IMAGERY ON A BOTTLE
• Logo Design: "Verdelle Garden Cocktails"
• Label: We can have front and back, or one continuous label. We are open to painted designs.
• The label must contain the following text in quotes:
• Product Name: " Verdelle Garden Cocktails "
• "15% Alc. by Vol. (30 proof)"
• "750 mL"
• "Handcrafted and Bottled by Harrow Creek Orchard Farm and Distillery
• Winchester, NH-USA"
• The following Text must be in all caps and 3mm in height:
• "Government Warning: (1) According to the Surgeon General, women should not drink alcoholic beverages during pregnancy because of the risk of birth defects. (2) Consumption of alcoholic beverages impairs your ability to drive a car or operate machinery and may cause health problems."
• Must be a space for a bar code: .75 in height by 1.25 in length.
• “www.harrowcreekorchard.example”
• Must Have the following Statement:
• Infused with fruit, herb, and floral botanicals and sweetened with stevia. Serve cold over ice.
Nice to have
• Antique or vintage botanical illustrations
• https://www.pinboardly.example/kestrawynn/garden-drinks/
• check out the board for inspiration.
• Think artisanal small batch spirits that are ready to drink out of the bottle. Refreshing flavors just pour over ice and add herb leaves.
• You can use images by doing a search here.
• http://archive.plantrecords.example/search.xhtml?start=0&collectionFacet=Orchard+Fruit+Painting+Set

```html
<!DOCTYPE html>
<html lang="en">
<head>
<meta charset="utf-8">
<title>Verdelle Garden Cocktails – Label Range</title>
<link rel="stylesheet" href="https://fonts.googleapis.com/css2?family=IM+Fell+DW+Pica&family=Michroma&family=Playfair+Display:wght@700&display=swap">
<style>
  :root {
    --backdrop: #ece6dc;
    --ink: #1b1b1b;
    --paper: #ffffff;
    --berry-tone: #9467ee;
    --berry-soft: #c9b3f7;
    --citrus-tone: #22dc22;
    --citrus-soft: #a9e9b0;
    --pear-tone: #f4bd2e;
    --pear-soft: #e6d06a;
    --rule-red: #e84a4a;
    --rule-gold: #f2c531;
    --rule-green: #3cc35a;
    --rule-blue: #3a8fe0;
    --rule-violet: #9a5ad8;
  }
  * { box-sizing: border-box; margin: 0; padding: 0; }
  html, body { width: 1200px; height: 856px; overflow: hidden; }
  body { background: var(--backdrop); }
  .label-range { position: relative; width: 1200px; height: 856px; }
  .label {
    position: absolute; top: 148px; width: 300px; height: 560px;
  }
  .label--berry { left: 110px; --tone: var(--berry-tone); --soft: var(--berry-soft); }
  .label--citrus { left: 450px; --tone: var(--citrus-tone); --soft: var(--citrus-soft); }
  .label--pear { left: 790px; --tone: var(--pear-tone); --soft: var(--pear-soft); }
  .label__frame { position: absolute; inset: 0; width: 300px; height: 560px; }
  .stop-paper { stop-color: var(--paper); }
  .stop-tone { stop-color: var(--tone); }
  .stop-r { stop-color: var(--rule-red); }
  .stop-g { stop-color: var(--rule-gold); }
  .stop-gr { stop-color: var(--rule-green); }
  .stop-b { stop-color: var(--rule-blue); }
  .stop-v { stop-color: var(--rule-violet); }
  .label__seal {
    position: absolute; left: 88px; top: 32px; width: 124px; height: 124px;
    border-radius: 50%; background: var(--soft);
    display: flex; align-items: center; justify-content: center;
  }
  .label__seal-name {
    font-family: "IM Fell DW Pica", serif; font-size: 24px; color: var(--paper);
  }
  .label__brand {
    position: absolute; left: 0; right: 0; top: 176px; text-align: center;
    font-family: "IM Fell DW Pica", serif; font-size: 54px; line-height: 1; color: var(--ink);
  }
  .label__line {
    position: absolute; left: 0; right: 0; top: 236px; text-align: center;
    font-family: "Michroma", sans-serif; font-size: 17px; line-height: 26px;
    letter-spacing: 1px; color: var(--ink);
  }
  .label__fruit {
    position: absolute; left: 78px; top: 300px; width: 144px; height: 150px;
    border-radius: 46% 46% 40% 40%;
  }
  .label--berry .label__fruit { background: radial-gradient(circle at 45% 45%, #5a2a55, #2a1a38 70%, rgba(60,40,80,0)); }
  .label--citrus .label__fruit { background: radial-gradient(circle at 50% 60%, #f07a20, #e2a022 45%, #3f6a2a 75%, rgba(60,100,40,0)); }
  .label--pear .label__fruit { background: radial-gradient(ellipse at 45% 60%, #e8b23a, #c76a2a 45%, #3a5a2a 75%, rgba(60,90,40,0)); }
  .label__flavor {
    position: absolute; left: 0; right: 0; top: 486px; text-align: center;
    font-family: "Playfair Display", serif; font-weight: 700; font-size: 28px; color: var(--ink);
  }
</style>
</head>
<body>
<main class="label-range">

  <section class="label label--berry">
    <svg class="label__frame" viewBox="0 0 300 560" aria-hidden="true">
      <defs>
        <linearGradient id="fill-berry" x1="0" y1="0" x2="0" y2="1">
          <stop offset="0.1" class="stop-paper"/><stop offset="1" class="stop-tone"/>
        </linearGradient>
        <linearGradient id="rule-berry" x1="0" y1="0" x2="1" y2="1">
          <stop offset="0" class="stop-r"/><stop offset="0.25" class="stop-g"/><stop offset="0.5" class="stop-gr"/><stop offset="0.75" class="stop-b"/><stop offset="1" class="stop-v"/>
        </linearGradient>
      </defs>
      <path d="M8,118 h14 C22,40 90,8 150,8 C210,8 278,40 278,118 h14 V536 a16 16 0 0 0 -16 16 H24 a16 16 0 0 0 -16 -16 Z" fill="url(#fill-berry)" stroke="url(#rule-berry)" stroke-width="2.5"/>
      <path d="M15,124 h13 C28,48 94,15 150,15 C206,15 272,48 272,124 h13 V530 a14 14 0 0 0 -14 14 H29 a14 14 0 0 0 -14 -14 Z" fill="none" stroke="#555" stroke-width="0.8"/>
    </svg>
    <div class="label__seal"><span class="label__seal-name">Verdelle</span></div>
    <h2 class="label__brand">Verdelle</h2>
    <p class="label__line">GARDEN<br>COCKTAILS</p>
    <div class="label__fruit" role="img" aria-label="Vintage botanical illustration of blackberries on the stem"></div>
    <p class="label__flavor">BERRY</p>
  </section>

  <section class="label label--citrus">
    <svg class="label__frame" viewBox="0 0 300 560" aria-hidden="true">
      <defs>
        <linearGradient id="fill-citrus" x1="0" y1="0" x2="0" y2="1">
          <stop offset="0.1" class="stop-paper"/><stop offset="1" class="stop-tone"/>
        </linearGradient>
        <linearGradient id="rule-citrus" x1="0" y1="0" x2="1" y2="1">
          <stop offset="0" class="stop-r"/><stop offset="0.25" class="stop-g"/><stop offset="0.5" class="stop-gr"/><stop offset="0.75" class="stop-b"/><stop offset="1" class="stop-v"/>
        </linearGradient>
      </defs>
      <path d="M8,118 h14 C22,40 90,8 150,8 C210,8 278,40 278,118 h14 V536 a16 16 0 0 0 -16 16 H24 a16 16 0 0 0 -16 -16 Z" fill="url(#fill-citrus)" stroke="url(#rule-citrus)" stroke-width="2.5"/>
      <path d="M15,124 h13 C28,48 94,15 150,15 C206,15 272,48 272,124 h13 V530 a14 14 0 0 0 -14 14 H29 a14 14 0 0 0 -14 -14 Z" fill="none" stroke="#555" stroke-width="0.8"/>
    </svg>
    <div class="label__seal"><span class="label__seal-name">Verdelle</span></div>
    <h2 class="label__brand">Verdelle</h2>
    <p class="label__line">GARDEN<br>COCKTAILS</p>
    <div class="label__fruit" role="img" aria-label="Vintage botanical illustration of oranges and limes with leaves"></div>
    <p class="label__flavor">citrus</p>
  </section>

  <section class="label label--pear">
    <svg class="label__frame" viewBox="0 0 300 560" aria-hidden="true">
      <defs>
        <linearGradient id="fill-pear" x1="0" y1="0" x2="0" y2="1">
          <stop offset="0.1" class="stop-paper"/><stop offset="1" class="stop-tone"/>
        </linearGradient>
        <linearGradient id="rule-pear" x1="0" y1="0" x2="1" y2="1">
          <stop offset="0" class="stop-r"/><stop offset="0.25" class="stop-g"/><stop offset="0.5" class="stop-gr"/><stop offset="0.75" class="stop-b"/><stop offset="1" class="stop-v"/>
        </linearGradient>
      </defs>
      <path d="M8,118 h14 C22,40 90,8 150,8 C210,8 278,40 278,118 h14 V536 a16 16 0 0 0 -16 16 H24 a16 16 0 0 0 -16 -16 Z" fill="url(#fill-pear)" stroke="url(#rule-pear)" stroke-width="2.5"/>
      <path d="M15,124 h13 C28,48 94,15 150,15 C206,15 272,48 272,124 h13 V530 a14 14 0 0 0 -14 14 H29 a14 14 0 0 0 -14 -14 Z" fill="none" stroke="#555" stroke-width="0.8"/>
    </svg>
    <div class="label__seal"><span class="label__seal-name">Verdelle</span></div>
    <h2 class="label__brand">Verdelle</h2>
    <p class="label__line">GARDEN<br>COCKTAILS</p>
    <div class="label__fruit" role="img" aria-label="Vintage botanical illustration of a pear with leaves"></div>
    <p class="label__flavor">PEAR</p>
  </section>

</main>
</body>
</html>
```